BRV Coffee bag (front and back)

We use black matte bags and have front and back labels. We have a logo but need an attractive and inviting label. The labels will be used for our entire line of coffees. We sell most of our coffee to foodservice establishments (Restaurants, Hotels, Bakeries, Bodegas) and we would like to have these establishments display our bags of coffee to sell retail.
The logo can be used as a whole or using any one of the three components (Logo, image, tag).

Target Market(s)

People who buy the coffee they brew at home from the local shop they get their morning latte.. We are a local coffee company, but we do not sell locally roasted coffee!

Industry/Entity Type

Food

Font styles to use
Other font styles liked:
• something that looks good with our trademarked BRV

Colors

Designer to choose colors to be used in the design.

Requirements
Must have
• Respect Trademarked logo
Nice to have
• It would be nice to have a design that can be used with other mediums (airpot wraps, java jackets, )
Should not have
• Real People

```html
<!DOCTYPE html>
<html lang="en">
<head>
<meta charset="utf-8">
<title>BRV Coffee Bag Labels</title>
<link rel="stylesheet" href="https://fonts.googleapis.com/css2?family=Barlow:wght@300;400;500;600;700&display=swap">
<style>
  :root {
    --stage: #ececec;
    --label-dark: #262425;
    --red: #e8232e;
    --white: #ffffff;
    --ink: #1f1f1f;
    --grey-border: #8a8a8a;
    --leaf: #5f5c5c;
    --leaf-light: #7a7676;
    --cherry: #9a5230;
  }
  * { margin: 0; padding: 0; box-sizing: border-box; }
  html, body { width: 1200px; height: 800px; overflow: hidden; }
  body {
    background: var(--stage);
    font-family: "Barlow", Arial, sans-serif;
    color: var(--ink);
    position: relative;
  }

  /* ---------- Front label ---------- */
  .front-label {
    position: absolute; left: 190px; top: 96px;
    width: 405px; height: 608px;
    background: var(--label-dark);
    border-radius: 20px;
    overflow: hidden;
  }
  .front-art {
    position: absolute; left: 0; top: 0; width: 405px; height: 222px;
    background: linear-gradient(90deg,
      var(--leaf) 0%, var(--cherry) 14%, var(--leaf-light) 30%, var(--leaf) 40%,
      var(--leaf) 60%, var(--cherry) 72%, var(--leaf-light) 86%, var(--cherry) 100%);
  }
  .front-ribbon {
    position: absolute; left: 158px; top: 0; width: 88px; height: 120px;
    background: var(--red);
  }
  .front-mark {
    position: absolute; left: 144px; top: 97px; width: 116px; height: 116px;
    border-radius: 50%; background: var(--red);
    border: 10px solid var(--label-dark);
  }
  .front-name {
    position: absolute; left: 0; top: 232px; width: 100%;
    text-align: center; color: var(--white);
    font-weight: 300; font-size: 108px; line-height: 1; letter-spacing: 4px;
  }
  .front-tagline {
    position: absolute; left: 0; top: 340px; width: 100%;
    text-align: center; color: var(--white);
    font-size: 11px; letter-spacing: 4.5px;
  }
  .product-box {
    position: absolute; left: 55px; top: 382px; width: 294px; height: 158px;
    background: var(--white);
    border: 3px solid var(--grey-border);
    border-radius: 8px;
    overflow: hidden;
  }
  .product-title {
    position: absolute; left: 18px; top: 12px;
    font-weight: 700; font-size: 31px; line-height: 35px;
    color: var(--ink); letter-spacing: 0.3px;
  }
  .product-meta {
    position: absolute; left: 0; bottom: 0; width: 100%; height: 64px;
    border-top: 2px solid var(--grey-border);
    display: flex;
  }
  .roast-type {
    width: 130px; background: var(--label-dark); color: var(--white);
    font-weight: 500; font-size: 19px; line-height: 21px;
    padding: 8px 0 0 18px;
  }
  .tasting-notes {
    flex: 1; font-size: 14.5px; line-height: 15.5px; color: #333;
    padding: 6px 0 0 15px; letter-spacing: 0.3px;
  }
  .quality-seal {
    position: absolute; left: 316px; top: 350px; width: 72px; height: 72px;
    border-radius: 50%; background: var(--white);
    border: 3px solid var(--red);
  }
  .net-weight {
    position: absolute; left: 0; bottom: 0; width: 100%; height: 52px;
    background: var(--white);
    text-align: center; line-height: 48px;
    font-weight: 500; font-size: 19px; color: var(--ink);
  }

  /* ---------- Back label ---------- */
  .back-label {
    position: absolute; left: 660px; top: 184px;
    width: 346px; height: 433px;
    background: var(--label-dark);
    border-radius: 20px;
    overflow: hidden;
  }
  .back-brand {
    position: absolute; left: 38px; top: 26px; height: 82px;
    display: flex; align-items: center; gap: 14px;
  }
  .back-mark {
    width: 80px; height: 80px; border-radius: 50%;
    border: 5px solid var(--red);
  }
  .back-name {
    color: var(--white); font-weight: 300; font-size: 72px; line-height: 1;
    letter-spacing: 3px;
  }
  .back-tagline {
    position: absolute; left: 150px; top: 103px;
    color: var(--white); font-size: 7.5px; letter-spacing: 3px;
  }
  .info-panel {
    position: absolute; left: 0; top: 132px; width: 100%; height: 258px;
    background: var(--white);
    border-top: 6px solid var(--red);
    border-bottom: 7px solid var(--red);
  }
  .back-art {
    position: absolute; left: 262px; top: 120px; width: 84px; height: 280px;
    background: linear-gradient(180deg,
      var(--leaf) 0%, var(--leaf-light) 25%, var(--cherry) 40%,
      var(--leaf) 60%, var(--leaf-light) 100%);
    border-radius: 40px 0 0 30px;
  }
  .info-section {
    position: absolute; left: 28px; display: flex; gap: 10px;
  }
  .info-section.brewing { top: 163px; }
  .info-section.storing { top: 244px; }
  .info-icon { width: 28px; height: 34px; margin-top: 2px; }
  .info-heading {
    color: var(--red); font-weight: 600; font-size: 11.5px; line-height: 13px;
  }
  .info-list { list-style: none; font-size: 11px; line-height: 13.6px; color: #222; }
  .info-list li { padding-left: 8px; text-indent: -7px; }
  .info-list li::before { content: "• "; }
  .distributor {
    position: absolute; left: 28px; top: 311px;
    font-size: 11px; line-height: 13.6px; color: #222;
  }
  .distributor strong { font-weight: 600; }
</style>
</head>
<body>

  <section class="front-label">
    <div class="front-art" role="img" aria-label="Illustrated coffee branches with grey leaves, white blossoms and ripe coffee cherries"></div>
    <div class="front-ribbon"></div>
    <div class="front-mark"></div>
    <div class="front-name">BRV</div>
    <div class="front-tagline">Brava Roasters Coffee</div>

    <div class="product-box">
      <h1 class="product-title">GRAND CREMA<br>ESPRESSO</h1>
      <div class="product-meta">
        <div class="roast-type">ESPRESSO<br>ROAST</div>
        <div class="tasting-notes">Notes:<br>A rich, classic<br>espresso blend</div>
      </div>
    </div>
    <div class="quality-seal"></div>

    <div class="net-weight">2 Lb. Whole Bean Coffee</div>
  </section>

  <section class="back-label">
    <div class="back-brand">
      <div class="back-mark"></div>
      <div class="back-name">BRV</div>
    </div>
    <div class="back-tagline">Brava Roasters Coffee</div>

    <div class="info-panel"></div>
    <div class="back-art" role="img" aria-label="Illustrated coffee branch with leaves, blossoms and coffee cherries"></div>

    <div class="info-section brewing">
      <svg class="info-icon" viewBox="0 0 28 34" aria-hidden="true">
        <rect x="2" y="1" width="22" height="5" fill="#222"/>
        <rect x="2" y="6" width="6" height="26" fill="#222"/>
        <rect x="2" y="29" width="24" height="4" fill="#222"/>
        <path d="M10 17 h12 v8 a3 3 0 0 1 -3 3 h-6 a3 3 0 0 1 -3 -3z" fill="none" stroke="#222" stroke-width="2"/>
        <rect x="12" y="8" width="10" height="5" fill="#222"/>
      </svg>
      <div>
        <div class="info-heading">BREWING</div>
        <ul class="info-list">
          <li>Use fresh filtered cold water</li>
          <li>Measure 2 tbsp. of coffee for<br>every 6 oz of water.</li>
          <li>Brew with water 195°F - 205°F.</li>
        </ul>
      </div>
    </div>

    <div class="info-section storing">
      <svg class="info-icon" viewBox="0 0 28 34" aria-hidden="true">
        <path d="M3 8 L14 3 L25 8 L14 13 Z" fill="none" stroke="#222" stroke-width="2"/>
        <path d="M3 12 L14 17 L25 12 V24 L14 29 L3 24 Z" fill="#222"/>
      </svg>
      <div>
        <div class="info-heading">STORING</div>
        <ul class="info-list">
          <li>Store in an airtight container<br>in a cool, dry place.</li>
          <li>Do not freeze.</li>
        </ul>
      </div>
    </div>

    <div class="distributor">
      Distributed by:<br>
      <strong>Riverbend Coffee Company, LLC.</strong><br>
      hello@riverbendcoffee.com<br>
      555-014-2290
    </div>
  </section>

</body>
</html>
```